San Francisco Leading Consulting firm - 47Nova Web Design Project

•Create a Web Design
•Uncoded webpage layout design
•2 Pages Design - Homepage + Interior Page

Task Description
Hello, we're looking for a re-design our current website www.47nova-example.com

we have a sample mockup design @

http://47nova.civicpane-example.org/

This shows the layout that we like and also a sample of 6 pictures that would change based on where you mouse over..

6 pictures HOME design needs to be included.

SMART
THOUGHTFUL
FLEXIBLE
CREATIVE SERVICES
TECHNICAL SERVICES
PARTNERS

sites we like:

http://www.brelmoradvisory-example.com/Home.cfm?id=Home
http://www.pixelquarry-example.com/index.html

Our company can be best described as: 100+ employees, cutting-edge, depandable, innovative, strong, smart.

Our Primary focus is: IT Consulting Services and Creative Design services

47Nova LLC is a consulting firm providing creative design, business and technology solutions to both private and public interests.

Established in 1996, 47Nova is a San Francisco based company providing specialists for a range of business needs including:

Creative Design Services
•Print
•Logo Design
•Website Design
•Illustration

and

Business and Technology solutions

•Application Software and Web Development
•Business Process Re-Design (BPR)
•Business/Systems Analysis and Requirement Documentation
•Mentoring and Training
•Network/Hardware Installation Services
•System Design and Architecture
•Vendor Management
•Teamvault Architecture and Implementation

our sample mockup site:

Reason: Due to holiday season, we're not available to work with designers and finilize our design.  

Thank you very much for submitting your design.

We appreciate your time and creativity.   Since, our office is currently closed for holidays, we will be reviewing it in details next week and will make our decision as soon as possible.

It would be great if you could submit any of your changes by Wed next week, so it would be part of our reviews. 

Please see updated wireframe under attachments:  we have some minor updates to our wireframe that we would like you to update your designs, if possible.  

We also encorouge you not to use our standard wireframe and come up with more unique designs.   Everything would be considered when we review your design.

 

Target Market(s)

Creative services and professional services clients, including government agencies

Industry/Entity Type

Business

Requirements
Must have
• Clean, professional look, easy navigation

```html
<!DOCTYPE html>
<html lang="en">
<head>
<meta charset="utf-8">
<title>47Nova – Home</title>
<link href="https://fonts.googleapis.com/css2?family=Arimo:wght@400;700&display=swap" rel="stylesheet">
<style>
:root{
  --header-bg:#e4edf6;
  --header-bg-2:#d6e2ef;
  --page-bg:#ffffff;
  --footer-bg:#dce6f0;
  --nav-blue:#1f5fa8;
  --accent:#2a9be0;
  --accent-dark:#1a6fb3;
  --frame:#cddbea;
  --frame-active:#3a78b8;
  --search-bar:#2c5f95;
  --hotline:#d0202a;
  --text:#222222;
  --rule:#444444;
}
*{margin:0;padding:0;box-sizing:border-box}
html,body{width:1200px;height:900px;overflow:hidden}
body{position:relative;background:var(--page-bg);font-family:"Arimo",Arial,sans-serif;color:var(--text)}

.site-header{position:absolute;left:0;top:0;width:1200px;height:116px;
  background:linear-gradient(180deg,var(--header-bg) 0%,var(--header-bg-2) 100%)}
.brand{position:absolute;left:164px;top:14px;display:flex;align-items:center;gap:10px}
.brand-mark{width:34px;height:34px;background:var(--accent-dark)}
.brand-name{font-size:34px;font-weight:400;color:#8d96a2;letter-spacing:1px}

.search-bar{position:absolute;left:786px;top:0;width:224px;height:32px;background:var(--search-bar);
  display:flex;align-items:center;padding:0 8px;gap:8px}
.search-field{width:140px;height:20px;background:#7fa3c9;border:1px solid #a9c3de;color:#fff;
  font-size:11px;font-weight:700;padding:2px 6px;line-height:14px}
.social-square{width:16px;height:16px;background:#ffffff;opacity:.85}
.social-square.alt{background:#5fbde9}

.hotline{position:absolute;left:810px;top:38px;font-size:15px;font-weight:700;color:var(--hotline);letter-spacing:.5px}
.hotline-icon{position:absolute;left:990px;top:10px}

.main-nav{position:absolute;left:164px;top:78px;width:872px;height:28px;border-bottom:1px solid #b9c9da;
  font-size:13px;color:var(--nav-blue)}
.main-nav a,.main-nav .sep{position:absolute;top:2px;color:var(--nav-blue);text-decoration:none;white-space:nowrap}
.main-nav a{padding:0 4px 6px}
.main-nav a.active{font-weight:700;border-bottom:3px solid var(--nav-blue)}

.slider{position:absolute;left:164px;top:134px;width:872px;height:410px;background:var(--frame)}
.slider-main{position:absolute;left:10px;top:10px;width:854px;height:292px;
  background:linear-gradient(100deg,#3b2c24 0%,#8a7461 30%,#d9d0c6 55%,#a68f78 78%,#6d5a4a 100%)}
.thumbs{position:absolute;left:10px;top:312px;display:flex;gap:14px}
.thumb{width:160px;height:90px;border:5px solid #b7cbe0}
.thumb.active{border-color:var(--frame-active)}
.thumb-pointer{position:absolute;left:344px;top:302px}

.content-col{position:absolute;top:566px}
.col-left{left:164px;width:278px}
.col-bottom{left:456px;width:270px}
.col-right{left:746px;width:278px}
.col-title{font-size:12px;font-weight:700;color:var(--accent);text-transform:uppercase;
  padding-bottom:6px;border-bottom:2px solid var(--accent)}
.teaser{display:flex;gap:16px;height:84px;margin-top:16px}
.teaser + .teaser{margin-top:18px;border-top:1px dashed var(--rule);padding-top:18px;height:120px}
.teaser-img{flex:0 0 90px;height:84px}
.teaser-body{width:164px}
.teaser-title{font-size:11px;font-weight:700;color:var(--accent);margin:2px 0 6px}
.teaser-text{font-size:10px;line-height:16px;color:var(--text)}
.teaser-text a{color:var(--accent-dark);font-weight:700;text-decoration:none}

.site-footer{position:absolute;left:0;top:850px;width:1200px;height:50px;background:var(--footer-bg);
  font-size:10px;color:#4a4f57;font-weight:700}
.copyright{position:absolute;left:164px;top:20px}
.follow{position:absolute;left:912px;top:16px;display:flex;align-items:center;gap:8px}
.follow .social-square{background:#3b5a9a;opacity:1}
.follow .social-square.alt{background:#5fbde9}
</style>
</head>
<body>

<header class="site-header">
  <div class="brand"><span class="brand-mark"></span><span class="brand-name">47Nova</span></div>

  <div class="search-bar">
    <div class="search-field">Search...</div>
    <span class="social-square"></span>
    <span class="social-square alt"></span>
  </div>

  <div class="hotline">Hotline (+01) 555010247</div>
  <svg class="hotline-icon" width="40" height="70" viewBox="0 0 40 70" aria-hidden="true">
    <path d="M20 4 C6 6 4 30 10 48 C14 60 22 66 30 64 L32 56 L24 52 L20 58 C14 50 12 30 16 18 L24 18 L26 8 Z" fill="var(--hotline)"/>
  </svg>

  <nav class="main-nav">
    <a class="active" href="#" style="left:0">Home</a><span class="sep" style="left:60px">:</span>
    <a href="#" style="left:76px">Company</a><span class="sep" style="left:152px">:</span>
    <a href="#" style="left:168px">Technical Services</a><span class="sep" style="left:310px">:</span>
    <a href="#" style="left:326px">Creative Services</a><span class="sep" style="left:460px">:</span>
    <a href="#" style="left:476px">Partners</a><span class="sep" style="left:550px">:</span>
    <a href="#" style="left:566px">Contact</a>
  </nav>
</header>

<section class="slider">
  <div class="slider-main" role="img" aria-label="Photo of business team reviewing documents in an office"></div>
  <svg class="thumb-pointer" width="20" height="10" viewBox="0 0 20 10" aria-hidden="true"><path d="M0 10 L10 0 L20 10 Z" fill="var(--frame-active)"/></svg>
  <div class="thumbs">
    <div class="thumb" role="img" aria-label="Abstract blue technology image" style="background:linear-gradient(135deg,#f2f6fa,#9fc2dd)"></div>
    <div class="thumb" role="img" aria-label="Business people shaking hands" style="background:linear-gradient(135deg,#cfcac4,#6e6a66)"></div>
    <div class="thumb active" role="img" aria-label="Team meeting photo" style="background:linear-gradient(135deg,#5a4a3e,#d3c8bb)"></div>
    <div class="thumb" role="img" aria-label="Laptop and broadband graphic" style="background:linear-gradient(135deg,#ffffff,#8fc3e6)"></div>
    <div class="thumb" role="img" aria-label="Solutions word graphic" style="background:linear-gradient(135deg,#e6e6e6,#9a9a9a)"></div>
  </div>
</section>

<section class="content-col col-left">
  <h2 class="col-title">Left Content</h2>
  <article class="teaser">
    <div class="teaser-img" role="img" aria-label="Colourful glowing abstract artwork" style="background:radial-gradient(circle,#ffe9f2 0%,#e86aa6 40%,#e38a2a 100%)"></div>
    <div class="teaser-body"><h3 class="teaser-title">EXAMPLE TEXT</h3>
    <p class="teaser-text">Lorem ipsum dolor sit amet, consec adipiscing elit. Sed eu typo orci netus. Sed pretium ac ante nulla pulvinar. <a href="#">Read more</a></p></div>
  </article>
  <article class="teaser">
    <div class="teaser-img" role="img" aria-label="Dancer in motion on grey background" style="background:linear-gradient(135deg,#eeeeee,#5d6670)"></div>
    <div class="teaser-body"><h3 class="teaser-title">EXAMPLE TEXT</h3>
    <p class="teaser-text">Lorem ipsum dolor sit amet, consec adipiscing elit. Sed eu typo orci netus. Sed pretium ac ante nulla pulvinar. <a href="#">Read more</a></p></div>
  </article>
</section>

<section class="content-col col-bottom">
  <h2 class="col-title">Bottom Content</h2>
  <article class="teaser">
    <div class="teaser-img" role="img" aria-label="Cabin in a green landscape at dusk" style="background:linear-gradient(180deg,#2d3a3f 0%,#7c8f6a 60%,#3f5a2a 100%)"></div>
    <div class="teaser-body"><h3 class="teaser-title">EXAMPLE TEXT</h3>
    <p class="teaser-text">Lorem ipsum dolor sit amet, consec adipiscing elit. Sed eu typo orci netus. Sed pretium ac ante nulla pulvinar. <a href="#">Read more</a></p></div>
  </article>
  <article class="teaser">
    <div class="teaser-img" role="img" aria-label="Tree in a golden field" style="background:linear-gradient(180deg,#f4efc2 0%,#d9c05a 60%,#8a8a2c 100%)"></div>
    <div class="teaser-body"><h3 class="teaser-title">EXAMPLE TEXT</h3>
    <p class="teaser-text">Lorem ipsum dolor sit amet, consec adipiscing elit. Sed eu typo orci netus. Sed pretium ac ante nulla pulvinar. <a href="#">Read more</a></p></div>
  </article>
</section>

<section class="content-col col-right">
  <h2 class="col-title">Right Content</h2>
  <article class="teaser">
    <div class="teaser-img" role="img" aria-label="Golden light burst on dark background" style="background:radial-gradient(circle,#f3e7a0 0%,#9a7a2a 35%,#1e1a10 100%)"></div>
    <div class="teaser-body"><h3 class="teaser-title">EXAMPLE TEXT</h3>
    <p class="teaser-text">Lorem ipsum dolor sit amet, consec adipiscing elit. Sed eu typo orci netus. Sed pretium ac ante nulla pulvinar. <a href="#">Read more</a></p></div>
  </article>
  <article class="teaser">
    <div class="teaser-img" role="img" aria-label="Grey abstract 3D typography artwork" style="background:linear-gradient(135deg,#d8d8d8,#4b4b4b)"></div>
    <div class="teaser-body"><h3 class="teaser-title">EXAMPLE TEXT</h3>
    <p class="teaser-text">Lorem ipsum dolor sit amet, consec adipiscing elit. Sed eu typo orci netus. Sed pretium ac ante nulla pulvinar. <a href="#">Read more</a></p></div>
  </article>
</section>

<footer class="site-footer">
  <p class="copyright">Copyright © 2010 Copyright 2010, 47Nova, LLC All rights reserved.</p>
  <div class="follow">Follow me on <span class="social-square"></span><span class="social-square alt"></span></div>
</footer>

</body>
</html>
```